Business Card Design

Lotside Ledger is an online automotive resource on a national scale specifically targeting lease purchases for new cars. Our Online and app platform allow prospective lease clients to scan a window sticker while at a franchise dealership and instantly receive a lease quote at what we call the sweet spot. Lotside Ledger offers price transparency during the lease process to allow average people the confidence in the lease process and takes away any fear of the big franchise dealers.
Lotside ledger allows ordinary lease customers to know they are getting a low price lease and not overpaying. Never overpay again

Industry/Entity Type

Automotive

Contact Information for Business Card

Lotside Ledger
Marcus Todwell (President of operations)
Phone: 888-302-7716
Cell: 561-448-2053

```html
<!DOCTYPE html>
<html lang="en">
<head>
<meta charset="utf-8">
<title>Lotside Ledger – Business Card</title>
<link rel="stylesheet" href="https://fonts.googleapis.com/css2?family=Open+Sans:ital,wght@0,400;0,800;1,400&display=swap">
<style>
  :root {
    --page-bg: #e9e7e4;
    --card-dark: #3b3b3d;
    --card-light: #ffffff;
    --swoosh-grey: #c9c9c9;
    --logo-ink: #1f1f1f;
    --text-light: #f2f2f2;
    --icon-bg: #ffffff;
    --icon-ink: #3b3b3d;
  }
  html, body {
    margin: 0;
    width: 1200px;
    height: 900px;
    overflow: hidden;
    background: var(--page-bg);
    font-family: "Open Sans", Arial, sans-serif;
  }
  .stage {
    position: relative;
    width: 1200px;
    height: 900px;
  }
  .card {
    position: absolute;
    top: 300px;
    width: 500px;
    height: 300px;
    border-radius: 40px;
    overflow: hidden;
    box-shadow: 0 10px 30px rgba(0,0,0,0.18);
  }
  .card-front { left: 70px; background: var(--card-dark); }
  .card-back { left: 630px; background: var(--card-light); }
  .card-shape { position: absolute; inset: 0; }
  .holder {
    position: absolute;
    left: 34px;
    top: 26px;
    color: var(--text-light);
  }
  .holder-name {
    font-size: 19px;
    font-style: italic;
    margin: 0;
  }
  .holder-title {
    font-size: 14px;
    font-style: italic;
    margin: 4px 0 0;
  }
  .contact-list {
    position: absolute;
    left: 30px;
    top: 168px;
    list-style: none;
    margin: 0;
    padding: 0;
    color: var(--text-light);
    font-size: 13px;
  }
  .contact-item {
    display: flex;
    align-items: center;
    gap: 8px;
    height: 22px;
    white-space: nowrap;
  }
  .contact-icon { width: 14px; height: 14px; flex: none; }
  .logo {
    position: absolute;
    display: flex;
    align-items: center;
    gap: 10px;
    color: var(--logo-ink);
  }
  .logo-mark {
    width: 16px;
    height: 16px;
    border-radius: 50%;
    background: var(--logo-ink);
    flex: none;
  }
  .logo-name {
    font-weight: 800;
    text-transform: uppercase;
    line-height: 0.95;
    letter-spacing: 0.5px;
  }
  .card-front .logo { left: 290px; top: 120px; }
  .card-front .logo-name { font-size: 24px; }
  .card-back .logo { left: 120px; top: 112px; }
  .card-back .logo-name { font-size: 34px; }
</style>
</head>
<body>
<main class="stage">

  <section class="card card-front" aria-label="Card front">
    <svg class="card-shape" viewBox="0 0 500 300" aria-hidden="true">
      <g transform="translate(40 0)">
        <path d="M230 300 C 150 230, 170 110, 260 60 C 330 20, 420 20, 500 40 L 500 300 Z" fill="var(--swoosh-grey)"/>
        <path d="M250 300 C 185 230, 200 120, 280 75 C 350 40, 430 40, 500 60 L 500 300 Z" fill="var(--card-light)"/>
      </g>
      <rect x="500" y="0" width="40" height="300" fill="var(--card-light)"/>
    </svg>
    <div class="holder">
      <p class="holder-name">Dario Kelvane</p>
      <p class="holder-title">Director</p>
    </div>
    <ul class="contact-list">
      <li class="contact-item">
        <svg class="contact-icon" viewBox="0 0 14 14" aria-hidden="true"><circle cx="7" cy="7" r="7" fill="var(--icon-bg)"/><path d="M4.5 3.5 L6 3.5 L6.5 5.5 L5.6 6.2 Q6.4 7.8 7.8 8.4 L8.5 7.5 L10.5 8 L10.5 9.5 Q6 10.5 4.5 3.5 Z" fill="var(--icon-ink)"/></svg>
        <span>888-302-7716</span>
      </li>
      <li class="contact-item">
        <svg class="contact-icon" viewBox="0 0 14 14" aria-hidden="true"><circle cx="7" cy="7" r="7" fill="var(--icon-bg)"/><rect x="5" y="3" width="4" height="8" rx="0.8" fill="var(--icon-ink)"/></svg>
        <span>561-448-2053</span>
      </li>
      <li class="contact-item">
        <svg class="contact-icon" viewBox="0 0 14 14" aria-hidden="true"><circle cx="7" cy="7" r="7" fill="var(--icon-bg)"/><rect x="3.5" y="4.5" width="7" height="5" fill="var(--icon-ink)"/><path d="M3.5 4.5 L7 7.5 L10.5 4.5" stroke="var(--icon-bg)" stroke-width="0.8" fill="none"/></svg>
        <span>you@lotsideledger.test</span>
      </li>
    </ul>
    <div class="logo">
      <span class="logo-mark"></span>
      <span class="logo-name">Lotside<br>Ledger</span>
    </div>
  </section>

  <section class="card card-back" aria-label="Card back">
    <div class="logo">
      <span class="logo-mark"></span>
      <span class="logo-name">Lotside<br>Ledger</span>
    </div>
  </section>

</main>
</body>
</html>
```